Letter head / email signature/ contract document templates

We need a professional email signature and letterhead designed for our established carpentry and maintenance company. Our Logo (attached) was originally designed 6 years ago by design guru and we love it, looking for something to compliment it ( not a home job)

```html
<!DOCTYPE html>
<html lang="en">
<head>
<meta charset="utf-8">
<title>Harbourline Maintenance – Stationery</title>
<link href="https://fonts.googleapis.com/css2?family=Open+Sans:wght@400;600;700&display=swap" rel="stylesheet">
<style>
  :root {
    --bg: #ebebed;
    --paper: #ffffff;
    --ink: #555659;
    --charcoal: #323234;
    --red: #d81e26;
  }
  * { box-sizing: border-box; margin: 0; padding: 0; }
  html, body { width: 1200px; height: 800px; overflow: hidden; }
  body {
    background: var(--bg);
    font-family: "Open Sans", Arial, sans-serif;
    color: var(--ink);
    position: relative;
  }

  /* Shared brand lockup */
  .brand {
    position: absolute; left: 0; right: 0;
    display: flex; align-items: center; justify-content: center; gap: 8px;
    font-weight: 700; color: var(--charcoal);
    white-space: nowrap;
  }
  .brand-mark { background: var(--red); flex: none; }

  /* Letterhead */
  .letterhead {
    position: absolute; left: 150px; top: 40px;
    width: 510px; height: 720px;
    background: var(--paper);
    box-shadow: 0 2px 10px rgba(0,0,0,.08);
    overflow: hidden;
  }
  .letterhead .brand { top: 58px; font-size: 17px; }
  .letterhead .brand-mark { width: 14px; height: 14px; }

  .contact {
    position: absolute; right: 48px; top: 130px;
    font-size: 9px; line-height: 1.55; color: var(--ink); font-style: normal;
  }
  .contact-line { display: flex; align-items: center; gap: 5px; }
  .contact-line svg { width: 8px; height: 8px; flex: none; }

  .letter-body {
    position: absolute; left: 48px; top: 130px; width: 414px;
    font-size: 8.5px; line-height: 1.6;
  }
  .salutation { margin-bottom: 64px; }
  .para { margin-bottom: 10px; }
  .signoff { margin-top: 4px; }
  .signature {
    display: block; width: 80px; height: 34px; margin-top: 12px;
    background: linear-gradient(90deg, #f2f2f3, #e6e6e8);
    border-radius: 3px;
  }

  .footer-dark {
    position: absolute; left: 0; bottom: 0; width: 290px; height: 10px;
    background: var(--charcoal);
  }
  .footer-red {
    position: absolute; right: 0; bottom: 0; width: 230px; height: 34px;
    background: var(--red);
    color: #fff; font-size: 12px;
    display: flex; align-items: center; justify-content: center;
  }

  /* Business cards */
  .card {
    position: absolute; left: 820px;
    width: 190px; height: 330px;
    box-shadow: 0 2px 10px rgba(0,0,0,.1);
    overflow: hidden;
  }
  .card-front { top: 40px; background: var(--paper); }
  .card-back { top: 420px; background: var(--charcoal); }
  .card .brand { top: 128px; font-size: 11px; gap: 6px; }
  .card .brand-mark { width: 9px; height: 9px; }
  .card-back .brand { color: #fff; }
  .card-url {
    position: absolute; left: 0; right: 0; bottom: 44px;
    text-align: center; font-size: 8px; color: var(--charcoal);
  }
  .card-back .card-url { color: #fff; }
  .card-url .accent { color: var(--red); }
</style>
</head>
<body>

  <section class="letterhead">
    <div class="brand"><span class="brand-mark"></span>Harbourline Maintenance</div>

    <address class="contact">
      <div>48 Cedar Hollow Road,</div>
      <div>Brookfield, ON K2M 4T7</div>
      <div class="contact-line">
        <svg viewBox="0 0 10 10"><path fill="#d81e26" d="M2 1h2l1 2.5-1.3 1a6 6 0 0 0 2.8 2.8l1-1.3L10 7v2a1 1 0 0 1-1 1A9 9 0 0 1 0 1a1 1 0 0 1 1-1z"/></svg>
        555.204.7788
      </div>
      <div class="contact-line">
        <svg viewBox="0 0 10 10"><rect x="0" y="2" width="10" height="7" fill="#d81e26"/><path d="M0 2l5 4 5-4" stroke="#fff" stroke-width="1" fill="none"/></svg>
        hello@harbourlinefix.com
      </div>
    </address>

    <div class="letter-body">
      <p class="salutation">Dear customer,</p>
      <p class="para">Lorem ipsum dolor sit amet, consectetur adipisicing elit, sed do eiusmod tempor incididunt ut labore et dolore magna aliqua. Ut enim ad minim veniam, quis nostrud exercitation ullamco laboris nisi ut aliquip ex ea commodo consequat. Duis aute irure dolor in reprehenderit in voluptate velit esse cillum dolore eu fugiat nulla pariatur. Excepteur sint occaecat cupidatat non proident, sunt in culpa qui officia deserunt mollit anim id est laborum.</p>
      <p class="para">Lorem ipsum dolor sit amet, consectetur adipisicing elit, sed do eiusmod tempor incididunt ut labore et dolore magna aliqua. Ut enim ad minim veniam, quis nostrud exercitation ullamco laboris nisi ut aliquip ex ea commodo consequat. Duis aute irure dolor in reprehenderit in voluptate velit esse cillum dolore eu fugiat nulla pariatur. Excepteur sint occaecat cupidatat non proident, sunt in culpa qui officia deserunt mollit anim id est laborum.</p>
      <p class="para">Lorem ipsum dolor sit amet, consectetur adipisicing elit, sed do eiusmod tempor incididunt ut labore et dolore magna aliqua. Ut enim ad minim veniam, quis nostrud exercitation ullamco laboris nisi ut aliquip ex ea commodo consequat. Duis aute irure dolor in reprehenderit in voluptate velit esse cillum dolore eu fugiat nulla pariatur. Excepteur sint occaecat cupidatat non proident, sunt in culpa qui officia deserunt mollit anim id est laborum.</p>
      <p class="para">Lorem ipsum dolor sit amet, consectetur adipisicing elit, sed do eiusmod tempor incididunt ut labore et dolore magna aliqua. Ut enim ad minim veniam, quis nostrud exercitation ullamco laboris nisi ut aliquip ex ea commodo consequat. Duis aute irure dolor in reprehenderit.</p>
      <p class="signoff">Yours Sincerely,</p>
      <span class="signature" role="img" aria-label="Handwritten signature"></span>
    </div>

    <div class="footer-dark"></div>
    <div class="footer-red">www.harbourlinefix.com</div>
  </section>

  <section class="card card-front">
    <div class="brand"><span class="brand-mark"></span>Harbourline Maintenance</div>
    <div class="card-url">www.<span class="accent">harbourlinefix</span>.com</div>
  </section>

  <section class="card card-back">
    <div class="brand"><span class="brand-mark"></span>Harbourline Maintenance</div>
    <div class="card-url">www.<span class="accent">harbourlinefix</span>.com</div>
  </section>

</body>
</html>
```